Business Card Design Project 4 Construction Business

I am after a creative, but sleek and simple/ clean business card design. This design will form the basis of future items and might include a logo or simply a creative way to lay out the text of my company name 'kestrel ventures'
I like the simplicity of black and white however I would also be happy to see a splash of colour introduced somehow to give the text some interest and make it stand out.
I would like a double sided card.
I am young (ish!) and professional, offering construction and project management services, what I don't want is the traditional builders type card featuring a cheesy hammer/ saw image etc.
As the company name, kestrel ventures, suggests, we focus on working closely and collaboratively together, in synergy with all stakeholders involved in the projects that we undertake
Construction

```html
<!DOCTYPE html>
<html lang="en">
<head>
<meta charset="utf-8">
<title>Kestrel Ventures – Business Card</title>
<link rel="stylesheet" href="https://fonts.googleapis.com/css2?family=Didact+Gothic&display=swap">
<style>
  :root {
    --paper: #ffffff;
    --ink: #1c1c1c;
    --ink-soft: #2a2a2a;
    --accent: #c0152a;
    --frame: #6e6e6e;
    --rule: #1a1a1a;
    --shadow: rgba(0, 0, 0, 0.28);
    --brand-bg-start: #ffffff;
    --brand-bg-end: #ececec;
  }
  * { margin: 0; padding: 0; box-sizing: border-box; }
  html, body {
    width: 1200px;
    height: 653px;
    overflow: hidden;
    background: var(--paper);
  }
  .card {
    position: relative;
    width: 1200px;
    height: 653px;
    background: var(--paper);
    font-family: "Didact Gothic", "Century Gothic", sans-serif;
    color: var(--ink);
  }
  .card-frame {
    position: absolute;
    inset: 10px 11px;
    border: 3px solid var(--frame);
    border-radius: 4px;
  }
  .brand {
    position: absolute;
    left: 667px;
    top: 52px;
    width: 478px;
    height: 140px;
    background: linear-gradient(180deg, var(--brand-bg-start), var(--brand-bg-end));
    display: flex;
    align-items: center;
    justify-content: center;
    gap: 18px;
  }
  .brand-mark {
    width: 22px;
    height: 22px;
    background: var(--accent);
    flex: none;
  }
  .brand-name {
    font-size: 46px;
    color: var(--ink);
    white-space: nowrap;
  }
  .contact {
    position: absolute;
    left: 104px;
    top: 0;
    text-shadow: 2px 3px 4px var(--shadow);
  }
  .contact-name,
  .contact-role {
    position: absolute;
    left: 0;
    font-size: 33px;
    white-space: nowrap;
    color: var(--ink-soft);
  }
  .contact-name { top: 226px; }
  .contact-role { top: 276px; }
  .contact-rule {
    position: absolute;
    left: 104px;
    top: 336px;
    width: 383px;
    height: 4px;
    background: var(--rule);
  }
  .contact-phone {
    position: absolute;
    left: 0;
    top: 368px;
    font-size: 27px;
    white-space: nowrap;
  }
  .contact-address {
    position: absolute;
    left: 25px;
    top: 414px;
    font-size: 27px;
    line-height: 38px;
    font-style: normal;
    white-space: nowrap;
  }
  .contact-address span { display: block; }
  .contact-address .indent { padding-left: 22px; }
  .website {
    position: absolute;
    left: 0;
    width: 1200px;
    top: 578px;
    text-align: center;
    font-size: 31px;
    text-shadow: 2px 3px 4px var(--shadow);
    padding-left: 22px;
  }
</style>
</head>
<body>
  <main class="card">
    <div class="card-frame"></div>

    <div class="brand">
      <span class="brand-mark"></span>
      <span class="brand-name">Kestrel Ventures</span>
    </div>

    <div class="contact-rule"></div>
    <section class="contact">
      <p class="contact-name">Owen Carrick</p>
      <p class="contact-role">Director</p>
      <p class="contact-phone">Tel: 0400 555 123</p>
      <address class="contact-address">
        <span># 14, Carrow St,</span>
        <span class="indent">Beltana,</span>
        <span class="indent">NSW 2099.</span>
      </address>
    </section>

    <p class="website">www.kestrelventuresgroup.com.au</p>
  </main>
</body>
</html>
```